BUSINESS CARD - HALVERDINE RURAL SERVICES

I would like to create a business card for my fertilizer spreading business. I would like to incorporate my existing logo and also a description of the services offered. The business card will be given to farmers so must be kept simple but effective. It will also be left in stores so much also be eye catching in order to stand out from other cards.

Target Market(s)

FARMERS

Requirements
Must have
• FRONT OF CARD = EXISTING LOGO + "CUSTOMISED SPREADING" below the logo

REAR Of CARD = SERVICES OFFERED AND CONTACT DETAILS

- Bulk fertilizer including Lime, Gypsum, Manure & Compost
- Granular fertilizer including Single Super, Urea, Gran-am, & Custom Blends
- Modern equipment - Autosteer & Variable Rate Capable
- Friendly & Reliable Service
- Contact Gus: 0471 502 318
Nice to have
• utilize same color scheme as existing logo

```html
<!DOCTYPE html>
<html lang="en">
<head>
<meta charset="utf-8">
<title>Halverdine Rural Services – Business Card</title>
<link rel="stylesheet" href="https://fonts.googleapis.com/css2?family=Arimo:wght@400;700&family=Oswald:wght@500;600&display=swap">
<style>
  :root {
    --orange: #f59420;
    --charcoal: #58585a;
    --ink: #3f3f41;
    --paper: #ffffff;
    --backdrop: #1f1f1f;
    --rule: #bdbdbd;
  }
  * { margin: 0; padding: 0; box-sizing: border-box; }
  html, body { width: 1200px; height: 1015px; overflow: hidden; }
  body {
    background: var(--backdrop);
    font-family: "Arimo", Arial, sans-serif;
    position: relative;
  }
  .card {
    position: absolute;
    left: 170px;
    width: 860px;
    height: 470px;
    overflow: hidden;
    box-shadow: 0 10px 30px rgba(0,0,0,.55);
  }
  .card--back { top: 25px; background: var(--orange); }
  .card--front { top: 520px; background: var(--paper); }

  .back-art { position: absolute; inset: 0; width: 100%; height: 100%; }

  /* Front */
  .brand {
    position: absolute;
    left: 70px; top: 150px;
    width: 340px;
    display: flex; align-items: center; gap: 16px;
  }
  .brand__dot {
    flex: none; width: 74px; height: 74px; border-radius: 50%;
    background: var(--charcoal);
  }
  .brand__name {
    font-weight: 700; font-size: 30px; line-height: 1.05;
    color: var(--charcoal); letter-spacing: -0.5px;
  }
  .divider {
    position: absolute; left: 440px; top: 60px;
    width: 1px; height: 240px; background: var(--rule);
  }
  .services {
    position: absolute; left: 470px; top: 56px; width: 370px;
    list-style: none; color: var(--ink);
    font-size: 17px; line-height: 1.32;
  }
  .services li { position: relative; padding-left: 22px; margin-bottom: 8px; }
  .services li::before {
    content: ""; position: absolute; left: 0; top: 6px;
    width: 11px; height: 11px; border-radius: 50%; background: var(--orange);
  }
  .tagline-band {
    position: absolute; left: 0; bottom: 0; width: 440px; height: 82px;
    background: var(--charcoal);
    display: flex; align-items: center; padding-left: 30px;
  }
  .tagline {
    font-family: "Oswald", "Arial Narrow", sans-serif; font-weight: 600;
    font-size: 36px; color: var(--orange); letter-spacing: .5px; white-space: nowrap;
  }
  .contact-band {
    position: absolute; right: 0; bottom: 0; width: 420px; height: 170px;
    background: var(--orange);
    display: flex; align-items: center; gap: 16px; padding-left: 26px;
  }
  .contact-icon { width: 54px; height: 54px; flex: none; }
  .contact {
    font-family: "Oswald", "Arial Narrow", sans-serif; font-weight: 600;
    font-size: 34px; color: var(--paper); white-space: nowrap;
  }
</style>
</head>
<body>

  <section class="card card--back" aria-label="Card back">
    <svg class="back-art" viewBox="0 0 860 470" aria-hidden="true">
      <polygon points="0,0 260,0 860,330 860,470 0,470" fill="var(--charcoal)"/>
      <circle cx="400" cy="215" r="170" fill="var(--orange)"/>
    </svg>
  </section>

  <section class="card card--front" aria-label="Card front">
    <div class="brand">
      <span class="brand__dot" aria-hidden="true"></span>
      <span class="brand__name">HALVERDINE RURAL SERVICES</span>
    </div>

    <div class="divider" aria-hidden="true"></div>

    <ul class="services">
      <li>Bulk fertilizer including Lime<br>Gypsum, Manure &amp; Compost</li>
      <li>Granular fertilizer including Single<br>Super, Urea, Gran-am<br>Custom Blends</li>
      <li>Modern equipment<br>Autosteer &amp; Variable Rate Capable</li>
      <li>Friendly &amp; Reliable Service</li>
    </ul>

    <div class="tagline-band">
      <span class="tagline">CUSTOMISED SPREADING</span>
    </div>

    <div class="contact-band">
      <svg class="contact-icon" viewBox="0 0 56 56" aria-hidden="true">
        <circle cx="28" cy="28" r="25" fill="none" stroke="#fff" stroke-width="3"/>
        <path d="M20 17c2-1 3 0 4 2l2 4c1 2 0 3-1 4l-1 1c1 3 4 6 7 7l1-1c1-1 2-2 4-1l4 2c2 1 3 2 2 4-1 3-4 4-7 3-8-2-15-9-17-17-1-3 0-6 2-8z" fill="#fff"/>
      </svg>
      <span class="contact">GUS: 0471 502 318</span>
    </div>
  </section>

</body>
</html>
```